Packaging / Logo Design for Toddler Potty Liners

We need a packaging and logo design for a new company based in Atlanta called "BrimLeaf". We manufacture innovative, eco-friendly baby / toddler products. Our initial product is a flushable, biodegradable potty liner used for toddler potty training. We are looking for a modern / clean / eco-friendly packaging and logo design for this product. Each package will contain 20 liners. Box dimensions are as follows:

Length = 8.5in
Width = 5in
Height = 1.5in

The box will have a perforated top measuring 6.5 inches (see attached pictures). Liners will be folded inside and individually pulled out through the perforated top (similar to a Softora box). See attached pictures of similar box.

Packaging should appeal to parents as an easy to use, eco-friendly, sanitary solution to potty training. This product is an alternative to the conventional way of cleaning / disinfecting the potty after each use, a process that most parents dread!

The closest competitors are NeatPips (www.neatpips-example.com) and Lumbra (www.lumbra-example.com) - you can reference their websites to get an idea for the product and use. However, their liners are not flushable and that is the biggest differentiator of this product. Their packaging seems conventional and non-inspiring so we would like our design to stand out from theirs.

We would like to see creative, modern cardboard box designs which will make our brand stand out from the competition. We would like to use one of the following color schemes: 1) a modern green color on a white background, 2) a modern green color on plain cardboard background, or 3) white on a modern green background. May use one or two additional complementary colors. See attached modern green image for inspiration. We would like to see clean lines, text and illustrations. We are looking forward to seeing any cool ideas you may have!
Updates

Brief has been updated with our desired color schemes and pictures for inspiration.  Please read updated brief before beginning your design!  Thanks so much!

Industry/Entity Type

Biodegradable

Requirements
Must have
• The front of the package should include the following info:

Logo: BrimLeaf
Product Name: Flushable Potty Chair Liners
Clean and Convenient
Fits All Potty Chairs
Sewer and Septic Safe
Patent Pending
20 Single-Use Flushable Potty Chair Liners

Package should also have space for some simple instructions (preferably with illustrations). This can be placed on one of the sides of the box.
1. Place liner over clean, dry (underline the word dry) potty bowl.
2. After your toddler uses the potty, remove liner (do not tie) and flush.
3. Give your toddler a high five!

Please submit design considering all sides of the box!

```html
<!DOCTYPE html>
<html lang="en">
<head>
<meta charset="utf-8">
<title>BrimLeaf Flushable Potty Chair Liners – Box Dieline</title>
<link rel="stylesheet" href="https://fonts.googleapis.com/css2?family=Varela+Round&display=swap">
<style>
  :root {
    --leaf-green: #8cc63f;
    --leaf-light: #b8db6e;
    --leaf-pale: #d9ecb0;
    --leaf-text: #9cbf45;
    --water-blue: #1ca3e3;
    --slate-grey: #8a8a8d;
    --paper-white: #ffffff;
    --backdrop: #ffffff;
  }
  * { box-sizing: border-box; margin: 0; padding: 0; }
  html, body {
    width: 1052px; height: 1200px; overflow: hidden;
    background: var(--backdrop);
    font-family: "Varela Round", "Arial Rounded MT Bold", sans-serif;
  }
  .dieline { position: relative; width: 1052px; height: 1200px; }
  .panel { position: absolute; overflow: hidden; }
  .pattern-fill {
    position: absolute; inset: 0;
    background: linear-gradient(135deg, var(--leaf-light) 0%, var(--leaf-green) 50%, var(--leaf-pale) 100%);
  }
  .pattern-fill--soft {
    background: linear-gradient(135deg, #a9d25a 0%, var(--leaf-green) 55%, #a4cd55 100%);
  }
  .flap-top   { left: 146px; top: 0;     width: 757px; height: 135px; }
  .side-left  { left: 0;     top: 146px; width: 133px; height: 444px; }
  .front      { left: 146px; top: 146px; width: 757px; height: 444px; }
  .side-right { left: 917px; top: 146px; width: 135px; height: 444px; }
  .top-strip  { left: 146px; top: 604px; width: 757px; height: 133px; }
  .back       { left: 146px; top: 751px; width: 757px; height: 449px; }

  .brand-corner { position: absolute; left: 0; top: 0; width: 400px; height: 155px; }
  .brand {
    position: absolute; display: flex; align-items: center; gap: 12px;
    color: var(--slate-grey); line-height: 1;
  }
  .brand-mark { border-radius: 50%; background: var(--leaf-green); flex: none; }
  .front .brand { left: 22px; top: 40px; font-size: 56px; }
  .front .brand-mark { width: 46px; height: 46px; }

  .product-name { position: absolute; left: 13px; top: 167px; display: flex; flex-direction: column; gap: 20px; align-items: flex-start; }
  .product-name span {
    display: block; background: var(--paper-white); border-radius: 10px;
    height: 50px; line-height: 50px; padding: 0 10px;
    font-size: 40px; color: var(--leaf-text);
  }
  .product-name .product-key { color: var(--water-blue); }

  .count { position: absolute; right: 20px; top: 18px; color: var(--paper-white); font-size: 15px; font-weight: 700; }
  .benefits { position: absolute; right: 20px; top: 198px; list-style: none; text-align: right; }
  .benefits li { color: var(--paper-white); font-size: 23px; height: 65px; line-height: 30px; text-shadow: 0 0 1px rgba(255,255,255,.6); }

  .logo-card {
    position: absolute; left: 146px; top: 126px; width: 458px; height: 183px;
    background: var(--paper-white); border-radius: 14px;
  }
  .back .brand { left: 30px; top: 50px; font-size: 84px; gap: 22px; }
  .back .brand-mark { width: 84px; height: 84px; }
</style>
</head>
<body>
<main class="dieline">
  <section class="panel flap-top"><div class="pattern-fill" role="img" aria-label="Green and white swirl pattern"></div></section>
  <section class="panel side-left"><div class="pattern-fill" role="img" aria-label="Green and white swirl pattern"></div></section>

  <section class="panel front">
    <div class="pattern-fill pattern-fill--soft" role="img" aria-label="Soft green swirl pattern background"></div>
    <svg class="brand-corner" viewBox="0 0 400 155" aria-hidden="true">
      <path d="M0 0 H394 C386 70 330 140 170 148 L0 155 Z" fill="#ffffff"/>
    </svg>
    <div class="brand"><span class="brand-name">BrimLeaf</span><span class="brand-mark"></span></div>
    <p class="count">20 LINERS</p>
    <h1 class="product-name">
      <span class="product-key">Flushable</span>
      <span>Potty</span>
      <span>Chair</span>
      <span>Liners</span>
    </h1>
    <ul class="benefits">
      <li>Clean and Convenient</li>
      <li>Fits All Potty Chairs</li>
      <li>Sewer and Septic Safe</li>
      <li>Patent Pending</li>
    </ul>
  </section>

  <section class="panel side-right"><div class="pattern-fill" role="img" aria-label="Green and white swirl pattern"></div></section>
  <section class="panel top-strip"><div class="pattern-fill" role="img" aria-label="Green and white swirl pattern"></div></section>

  <section class="panel back">
    <div class="pattern-fill" role="img" aria-label="Green and white swirl pattern"></div>
    <div class="logo-card">
      <div class="brand"><span class="brand-name">BrimLeaf</span><span class="brand-mark"></span></div>
    </div>
  </section>
</main>
</body>
</html>
```